Harborlight Vitality Studio Business Cards and Stationary
Harborlight Vitality Studio
Harborlight Vitality Studio Business Cards and Stationary - Massage Therapy
Creative Brief
Use same font as used in my logo
Similar font as in the word Foundation, or whatever you feel is appropriate
Professional
Dr. Raymond Okafor, D.C.
Every Step Starts With Balance
none at the moment
877 Go Align (462-5446)
www.frontdesk@harborlightvitalitystudio.com
www.harborlightvitalitystudio.com
1.I would like my Logo on top 2. Every Step Starts With Balance 3. Dr. Raymond Okafor, D.C. 4. 877 Go Align (462-5446) 5.email the web site

```html
<!DOCTYPE html>
<html lang="en">
<head>
<meta charset="utf-8">
<title>Harborlight Vitality Studio Business Card</title>
<link rel="stylesheet" href="https://fonts.googleapis.com/css2?family=Raleway:wght@500;700;800&display=swap">
<style>
  :root {
    --page-bg: #e9e6e2;
    --card-white: #ffffff;
    --brand-blue: #2f6aa6;
    --band-blue-light: #3a7bbd;
    --band-blue-dark: #2a5c93;
    --accent-red: #c9383a;
    --text-white: #ffffff;
    --logo-blue: #2a8fc9;
  }
  html, body {
    margin: 0;
    width: 1200px;
    height: 900px;
    overflow: hidden;
    background: var(--page-bg);
    font-family: "Raleway", sans-serif;
  }
  .canvas {
    width: 1200px;
    height: 900px;
    display: flex;
    align-items: center;
    justify-content: center;
  }
  .business-card {
    position: relative;
    width: 980px;
    height: 560px;
    background: var(--card-white);
    box-shadow: 0 10px 30px rgba(0,0,0,0.18);
    overflow: hidden;
  }
  .logo-area {
    position: absolute;
    top: 0; left: 0; right: 0;
    height: 250px;
    display: flex;
    align-items: center;
    justify-content: center;
    gap: 22px;
  }
  .logo-dot {
    width: 58px;
    height: 58px;
    border-radius: 50%;
    background: var(--logo-blue);
  }
  .logo-name {
    font-weight: 800;
    font-size: 42px;
    color: var(--logo-blue);
    letter-spacing: 0.5px;
  }
  .divider-line {
    position: absolute;
    top: 250px; left: 0; right: 0;
    height: 5px;
    background: var(--accent-red);
  }
  .divider-tab {
    position: absolute;
    top: 254px;
    left: 118px;
  }
  .info-band {
    position: absolute;
    top: 255px; left: 0; right: 0;
    height: 215px;
    background: linear-gradient(180deg, var(--band-blue-light), var(--band-blue-dark));
  }
  .holder {
    position: absolute;
    left: 112px;
    top: 75px;
    color: var(--text-white);
  }
  .holder-name {
    margin: 0 0 10px;
    font-weight: 700;
    font-size: 19px;
  }
  .holder-tagline {
    margin: 0;
    font-weight: 500;
    font-size: 16px;
  }
  .contact-list {
    position: absolute;
    left: 520px;
    top: 38px;
    margin: 0;
    padding: 0;
    list-style: none;
    color: var(--text-white);
    font-size: 15px;
    font-weight: 500;
  }
  .contact-item {
    display: flex;
    align-items: center;
    gap: 12px;
    margin-bottom: 12px;
  }
  .contact-icon {
    width: 20px;
    height: 20px;
    flex: none;
  }
  .accent-band {
    position: absolute;
    top: 470px; left: 0; right: 0;
    height: 32px;
    background: var(--accent-red);
  }
  .base-band {
    position: absolute;
    top: 502px; left: 0; right: 0;
    bottom: 0;
    background: var(--band-blue-dark);
  }
</style>
</head>
<body>
<main class="canvas">
  <article class="business-card">
    <header class="logo-area">
      <span class="logo-dot"></span>
      <span class="logo-name">Harborlight Vitality Studio</span>
    </header>

    <div class="divider-line"></div>

    <section class="info-band">
      <div class="holder">
        <p class="holder-name">Dr. Raymond Okafor, D.C.</p>
        <p class="holder-tagline">Every Step Starts With Balance</p>
      </div>

      <ul class="contact-list">
        <li class="contact-item">
          <svg class="contact-icon" viewBox="0 0 20 20" aria-hidden="true">
            <circle cx="10" cy="10" r="10" fill="#ffffff"/>
            <path d="M7 5.5 L8.6 5.5 L9.3 8 L8.2 8.9 Q9.2 11 11.1 11.8 L12 10.7 L14.5 11.4 L14.5 13 Q14.5 14 13.4 14 Q6 13.5 6 6.6 Q6 5.5 7 5.5 Z" fill="#2f6aa6"/>
          </svg>
          <span>877 Go Align (462-5446)</span>
        </li>
        <li class="contact-item">
          <svg class="contact-icon" viewBox="0 0 20 20" aria-hidden="true">
            <circle cx="10" cy="10" r="10" fill="#ffffff"/>
            <rect x="5" y="6.5" width="10" height="7" fill="none" stroke="#2f6aa6" stroke-width="1.4"/>
            <path d="M5 6.5 L10 10.5 L15 6.5" fill="none" stroke="#2f6aa6" stroke-width="1.4"/>
          </svg>
          <span>www.frontdesk@harborlightvitalitystudio.com</span>
        </li>
        <li class="contact-item">
          <svg class="contact-icon" viewBox="0 0 20 20" aria-hidden="true">
            <circle cx="10" cy="10" r="10" fill="#ffffff"/>
            <circle cx="10" cy="10" r="5" fill="none" stroke="#2f6aa6" stroke-width="1.3"/>
            <ellipse cx="10" cy="10" rx="2.2" ry="5" fill="none" stroke="#2f6aa6" stroke-width="1.1"/>
            <line x1="5" y1="10" x2="15" y2="10" stroke="#2f6aa6" stroke-width="1.1"/>
          </svg>
          <span>www.harborlightvitalitystudio.com</span>
        </li>
      </ul>
    </section>

    <svg class="divider-tab" width="26" height="14" viewBox="0 0 26 14" aria-hidden="true">
      <polygon points="0,0 26,0 13,13" fill="#c9383a"/>
    </svg>

    <div class="accent-band"></div>
    <div class="base-band"></div>
  </article>
</main>
</body>
</html>
```